Lena Hartwell Web

Lena Hartwell is a singer/songwriter that has a presence in the market for over 20 years. She currently has a website, lenahartwell.example that needs a major makeover. IT needs to be reorganized to; 1) make it more user friendly; 2) enable multi-languages including; Spanish, French, Russian, Japanese, Chinese and Portuguese; 3) enable purchases online through a storefront of promotional merchandise and music tracks. She has a logo that needs an update, as well as we currently have a business card open on PixelBazaar for input. Working to re-brand, or refresh her brand.

Lena Hartwell is the next Rosa Delmont! She has 5 platinum records, Lumen Award nominations and tours with Harold Prescott globally and is Nora Vandermeer's key backup singer for 12 years.
Updates

Some common questions have come up.  Here is some further input:

1) Colors - No specific color in mind but probably earth tones.  Although at this point we''re completely open.  Mary likes classical style, Russian, French decor.  Paris architecture. Greek, Italian textures, Goddess like symbols from the Roman Empire, or the symbols and pomp of the British monarchy.  One name on tap for the new CD is "Lanterns Over Quiet Water"
2) Example website - I have not found a new one specifically, but what I don''t like about the existing one is it is not easy to navigate.  Needs to be streamlined and easy to navigate with a storefront for merchandise and music downloads.  
3) On Logo - We''re revamping a "Global" merchandise rollout logo.  We''ve also considered possibly modifying the old english "Hartwell" family crest which signifies royalty, but have not explored that too much.  The hexagon yellow logo on her current website, I was thinking of modifying to gold (brushed - or polished?), then taking the LH lettering using a fountain pen type look there the line thickness flows with pressure on the pen, then make the gold look like a pillow, with the letter making an impression into the gold pillow.  This expands to a high quality pin, blinged up broach with diamonds imbedded for example, Global label identity, tee shirts, label tag on fashion clothing etc etc. 
 4) One thing marketing has asked us to build is a routine video blog to reach out to fans in a personal way.  Short clips of daily activity, travel prep for shows, etc. Possibly a signup/fanpage where people get emails sent back whenever anything new is posted, like a video blog, new pics, new events.  A menu to choose what you get updates on. 

Thanks, Dennis

Target Market(s)

1) Fan base in Europe, Asia, Latin America and North America
2) Movie producers seeking soundtracks
3) Private clients seeking an outstanding performer for corporate events

Industry/Entity Type

Singer

Requirements
Must have
• Better organization into smaller pages. Items critical include: 1) music tracks, 2) ClipStream links, 3) photos & Video, 4) storefront to enable online merchandise purchase 5) a way to illustrate her genre from; gospel, to rock, funk, R&B, country,

```html
<!DOCTYPE html>
<html lang="en">
<head>
<meta charset="utf-8">
<title>Lena Hartwell — Rising Pop Star</title>
<link href="https://fonts.googleapis.com/css2?family=Roboto+Condensed:wght@400;700&family=Cormorant+Garamond:ital,wght@1,600&family=Advent+Pro:wght@200&family=Oswald:wght@500&display=swap" rel="stylesheet">
<style>
:root{
  --bg-black:#070605;
  --bg-dark:#0d0b09;
  --panel:#1b1a19;
  --panel-line:#2a2928;
  --footer:#1d1d1d;
  --orange:#f07a1c;
  --orange-light:#f49a45;
  --orange-dark:#c85e0e;
  --text-light:#e6e6e6;
  --text-mute:#b5b5b5;
  --gold-1:#b89450;
  --gold-2:#5c4421;
  --gold-3:#1e150a;
}
*{box-sizing:border-box;margin:0;padding:0}
html,body{width:964px;height:1200px;overflow:hidden;background:var(--bg-black)}
body{position:relative;font-family:"Roboto Condensed",Arial,sans-serif;color:var(--text-light)}
.abs{position:absolute}

/* header */
.site-header{left:0;top:0;width:964px;height:181px;background:linear-gradient(#0a0908,#050404)}
.brand-badge{left:153px;top:18px;width:134px;height:134px;border-radius:50%;background:#fff;box-shadow:0 0 22px 6px rgba(255,255,255,.35);display:flex;align-items:center;justify-content:center}
.brand-name{font-family:"Oswald",sans-serif;font-weight:500;font-size:20px;color:var(--orange);letter-spacing:.2px}
.share-btn{top:14px;height:23px;width:66px;border-radius:3px;font-family:Georgia,serif;font-size:10px;color:#fff;display:flex;align-items:center;justify-content:center;letter-spacing:.5px}
.share-a{left:374px;background:linear-gradient(#6f87ab,#3f5680)}
.share-b{left:444px;background:linear-gradient(#9fe0f2,#4bb6d9)}
.share-c{left:515px;background:linear-gradient(#e5504b,#b9211c)}
.lang-select{left:735px;top:11px;width:105px;height:23px;border:1px solid #2b2b2b;background:#111;border-radius:3px;font-size:10px;color:#8d8d8d;padding:5px 10px}
.lang-select svg{position:absolute;right:8px;top:8px}
.main-nav{top:67px;height:29px;display:flex;font-size:11px}
.main-nav a{position:absolute;top:0;height:29px;display:flex;align-items:center;justify-content:center;color:#ddd;text-decoration:none;background:linear-gradient(#2b2b2b,#151515);border-radius:2px}
.main-nav a.active{background:linear-gradient(var(--orange-light),var(--orange-dark));color:#231105}

/* hero */
.hero{left:0;top:181px;width:964px;height:404px;background:radial-gradient(ellipse at 60% 30%,var(--gold-1) 0%,var(--gold-2) 45%,var(--gold-3) 90%)}
.hero-name{left:132px;top:272px;font-family:"Cormorant Garamond",serif;font-style:italic;font-weight:600;font-size:82px;color:#0c0a08;line-height:1}
.hero-tag{left:132px;top:370px;font-family:"Advent Pro",sans-serif;font-weight:200;font-size:104px;color:#fff;line-height:1;letter-spacing:-2px}
.slider-dots{left:598px;top:566px;display:flex;gap:6px}
.slider-dots span{width:9px;height:9px;border-radius:50%;background:#e9e9e9}
.slider-dots span.on{background:var(--orange)}

/* media tabs */
.media-zone{left:0;top:585px;width:964px;height:343px;background:radial-gradient(ellipse at 50% 40%,#1a140d,var(--bg-dark) 70%)}
.tab{top:624px;height:29px;font-size:11px;display:flex;align-items:center;justify-content:center;border-radius:3px 3px 0 0;background:linear-gradient(var(--orange-light),var(--orange-dark));color:#2a1305}
.tab.current{background:var(--panel);color:var(--orange)}
.tab-panel{left:136px;top:653px;width:703px;height:238px;background:var(--panel);border-radius:0 4px 6px 6px}
.arrow-btn{top:671px;width:24px;height:23px;border-radius:2px;background:linear-gradient(var(--orange-light),var(--orange-dark));display:flex;align-items:center;justify-content:center}
.video-thumb{top:705px;width:209px;height:142px;border:1px solid #333}
.video-thumb .play{position:absolute;left:50%;top:50%;width:24px;height:22px;margin:-11px 0 0 -12px;background:#d8281c;border-radius:3px;display:flex;align-items:center;justify-content:center}
.thumb-a{left:152px;background:linear-gradient(135deg,#4a1f52,#8b2c63 45%,#2a1030)}
.thumb-b{left:380px;background:linear-gradient(160deg,#1a1a1f,#4a3a30 60%,#15110e)}
.thumb-c{left:611px;background:radial-gradient(ellipse at 40% 40%,#8a7040,#3a2c18 70%)}
.video-caption{top:860px;font-size:10px;color:var(--text-light)}

/* footer */
.site-footer{left:0;top:928px;width:964px;height:239px;background:var(--footer)}
.footer-title{top:941px;font-size:14px;color:var(--orange);text-transform:uppercase}
.drop-card{left:136px;top:972px;width:225px;height:33px;border-radius:3px;background:linear-gradient(#8a8a8a,#5d5d5d);padding:3px 9px;color:#222;line-height:1.15}
.drop-card b{font-size:12px;font-weight:700;display:block}
.drop-card small{font-size:10px}
.drop-card em{position:absolute;right:9px;top:11px;font-style:normal;font-size:9px;color:#444}
.social-label{left:135px;top:1044px;font-size:14px;color:#ddd}
.social-links{left:242px;top:1047px;font-size:10px;color:#ccc;display:flex;gap:7px}
.gallery-thumb{width:66px;height:61px;border:1px solid #444}
.g-mono{background:linear-gradient(135deg,#d9d9d9,#2a2a2a)}
.g-red{background:linear-gradient(160deg,#6d5a48,#b33a32 55%,#3a2a22)}
.g-amber{background:linear-gradient(135deg,#4a3310,#d6a12a 55%,#3b2608)}
.field{background:var(--panel);border:1px solid var(--panel-line);font-size:10px;color:#cfcfcf;padding:8px 7px}
.send-btn{left:671px;top:1074px;width:109px;height:26px;background:linear-gradient(var(--orange-light),var(--orange-dark));color:#1e0e03;font-weight:700;font-size:14px;display:flex;align-items:center;justify-content:center}
.copyright-bar{left:0;top:1167px;width:964px;height:33px;background:var(--orange);font-size:10px;color:#fff;display:flex;align-items:center;justify-content:center}
.copyright-bar span{color:#2a1305;margin-left:3px}
</style>
</head>
<body>

<header class="abs site-header"></header>
<div class="abs brand-badge"><span class="brand-name">Lena Hartwell</span></div>

<a class="abs share-btn share-a" aria-label="Share on FriendSpace">SHARE</a>
<a class="abs share-btn share-b" aria-label="Share on Chirper">SHARE</a>
<a class="abs share-btn share-c" aria-label="Share on ClipStream">SHARE</a>

<div class="abs lang-select">Select Language
  <svg width="9" height="6" viewBox="0 0 9 6"><path d="M0 0h9L4.5 6z" fill="#777"/></svg>
</div>

<nav class="abs main-nav">
  <a class="active" style="left:374px;width:53px">Home</a>
  <a style="left:433px;width:56px">About</a>
  <a style="left:495px;width:58px">Events</a>
  <a style="left:558px;width:54px">Video</a>
  <a style="left:618px;width:64px">Pictures</a>
  <a style="left:687px;width:84px">Discographic</a>
  <a style="left:776px;width:62px">Contact</a>
</nav>

<section class="abs hero" role="img" aria-label="Sepia concert photo of the singer performing on stage under spotlights"></section>
<h1 class="abs hero-name">Lena Hartwell</h1>
<p class="abs hero-tag">Rising pop Star</p>
<div class="abs slider-dots"><span class="on"></span><span></span><span></span><span></span><span></span></div>

<section class="abs media-zone"></section>
<div class="abs tab current" style="left:136px;width:86px">Latest Video</div>
<div class="abs tab" style="left:228px;width:80px">Latest Events</div>
<div class="abs tab" style="left:323px;width:96px">Latest Pictures</div>
<div class="abs tab" style="left:425px;width:126px">Purchase music Track</div>
<div class="abs tab-panel"></div>
<div class="abs arrow-btn" style="left:770px"><svg width="8" height="10" viewBox="0 0 8 10"><path d="M6 1L2 5l4 4" stroke="#2a1305" stroke-width="1.6" fill="none"/></svg></div>
<div class="abs arrow-btn" style="left:799px"><svg width="8" height="10" viewBox="0 0 8 10"><path d="M2 1l4 4-4 4" stroke="#2a1305" stroke-width="1.6" fill="none"/></svg></div>

<div class="abs video-thumb thumb-a" role="img" aria-label="Video still of a guitarist and the singer on a purple-lit stage"><span class="play"><svg width="9" height="10"><path d="M0 0l9 5-9 5z" fill="#fff"/></svg></span></div>
<div class="abs video-thumb thumb-b" role="img" aria-label="Video still of a performance with a pianist and singers"><span class="play"><svg width="9" height="10"><path d="M0 0l9 5-9 5z" fill="#fff"/></svg></span></div>
<div class="abs video-thumb thumb-c" role="img" aria-label="Sepia video still of the singer on stage"><span class="play"><svg width="9" height="10"><path d="M0 0l9 5-9 5z" fill="#fff"/></svg></span></div>
<p class="abs video-caption" style="left:153px">Video Headig Goes Here</p>
<p class="abs video-caption" style="left:381px">Video Headig Goes Here</p>
<p class="abs video-caption" style="left:612px">Video Headig Goes Here</p>

<footer class="abs site-footer"></footer>
<h2 class="abs footer-title" style="left:135px">Quick Links</h2>
<h2 class="abs footer-title" style="left:380px">Imgae Gallery</h2>
<h2 class="abs footer-title" style="left:612px">Contact Us</h2>

<div class="abs drop-card"><b>Drop Crate</b><small>Send your Sound</small><em>TuneHaven</em></div>
<p class="abs social-label">Social Media links :</p>
<div class="abs social-links"><span>Chirper</span><span>ClipStream</span><span>FriendSpace</span><span>Feedline</span></div>

<div class="abs gallery-thumb g-mono" style="left:380px;top:972px" role="img" aria-label="Black and white portrait photo"></div>
<div class="abs gallery-thumb g-red" style="left:452px;top:972px" role="img" aria-label="Photo of the singer in a red dress"></div>
<div class="abs gallery-thumb g-amber" style="left:523px;top:972px" role="img" aria-label="Warm-toned photo of the singer by a window"></div>
<div class="abs gallery-thumb g-amber" style="left:380px;top:1039px" role="img" aria-label="Warm-toned photo of the singer by a window"></div>
<div class="abs gallery-thumb g-mono" style="left:452px;top:1039px" role="img" aria-label="Black and white portrait photo"></div>
<div class="abs gallery-thumb g-red" style="left:523px;top:1039px" role="img" aria-label="Photo of the singer in a red dress"></div>

<div class="abs field" style="left:612px;top:972px;width:116px;height:28px">Name</div>
<div class="abs field" style="left:735px;top:972px;width:105px;height:28px">Email</div>
<div class="abs field" style="left:612px;top:1004px;width:228px;height:65px">Message</div>
<div class="abs send-btn">Send Message</div>

<div class="abs copyright-bar">All right are reserved by<span>lenahartwell.example</span></div>

</body>
</html>
```